Cool modern, tech Business card design

Looking for a new business card design for our Managed IT Services company. We would like 2 sides, with the logo one one side horizontally and then the information on the back in either vertical or horizontal. We want our colors from the logo incorporated but also would like to see the color gray in there as well.

Target Market(s)

IT, Information Technology, Tech, Service

Industry/Entity Type

It Service

Contact Information for Business Card

Carl Penner
Managing Partner
(P)555-271-4830 ext xxx
(F)555-271-4831
www.brixtelcore.com

Font styles to use
Sans Serif

Colors
959595
000000
ec1f27

Requirements
Must have
• Logo on one side with some nice design or pattern
• Information on back in either vertical or horizontal format
Nice to have
• For it to look cool, tech, modern, stand out.

```html
<!DOCTYPE html>
<html lang="en">
<head>
<meta charset="utf-8">
<title>Brixtelcore Business Card</title>
<link rel="stylesheet" href="https://fonts.googleapis.com/css2?family=Montserrat:wght@400;500;800&display=swap">
<style>
  :root {
    --brand-red: #ec1f27;
    --brand-black: #000000;
    --brand-gray: #959595;
    --card-dark: #2b2b2b;
    --card-dark-edge: #1c1c1c;
    --card-light: #f7f7f7;
    --ink: #1a1a1a;
    --stage: #e4e4e4;
  }
  * { box-sizing: border-box; margin: 0; padding: 0; }
  html, body {
    width: 1200px;
    height: 856px;
    overflow: hidden;
    background: var(--stage);
    font-family: "Montserrat", Arial, sans-serif;
  }
  .canvas {
    position: relative;
    width: 1200px;
    height: 856px;
  }
  .card {
    position: absolute;
    width: 525px;
    height: 300px;
    border-radius: 4px;
    box-shadow: 0 10px 28px rgba(0,0,0,0.22);
  }

  /* Front side */
  .card--front {
    left: 60px;
    top: 110px;
    background: var(--card-dark);
    border: 1px solid var(--card-dark-edge);
    display: flex;
    align-items: center;
    justify-content: center;
  }
  .wordmark__name {
    font-weight: 500;
    letter-spacing: -0.5px;
    white-space: nowrap;
  }
  .card--front .wordmark__name {
    font-size: 50px;
    color: var(--brand-gray);
  }

  /* Back side */
  .card--back {
    left: 615px;
    top: 446px;
    background: var(--card-light);
    display: flex;
    align-items: center;
    padding: 0 30px;
  }
  .brand-panel {
    width: 220px;
    display: flex;
    justify-content: center;
  }
  .card--back .wordmark__name {
    font-size: 30px;
    color: var(--ink);
  }
  .divider {
    width: 1px;
    height: 170px;
    background: var(--brand-gray);
    margin: 0 22px 0 10px;
  }
  .contact {
    color: var(--ink);
    font-size: 12px;
    line-height: 1.4;
  }
  .contact__name {
    font-size: 20px;
    font-weight: 800;
    letter-spacing: 0.2px;
    line-height: 1.1;
  }
  .contact__title {
    font-size: 12px;
    margin-bottom: 10px;
  }
  .contact__address { margin-bottom: 6px; }
  .contact__list { list-style: none; }
  .contact__item {
    display: flex;
    align-items: center;
    gap: 8px;
  }
  .contact__icon {
    width: 11px;
    height: 11px;
    flex: none;
    fill: none;
    stroke: var(--brand-red);
    stroke-width: 1.6;
  }
  .contact__icon--solid { fill: var(--brand-red); stroke: none; }
</style>
</head>
<body>
<main class="canvas">
  <section class="card card--front" aria-label="Card front">
    <span class="wordmark__name">brixtelcore</span>
  </section>

  <section class="card card--back" aria-label="Card back">
    <div class="brand-panel">
      <span class="wordmark__name">brixtelcore</span>
    </div>
    <div class="divider"></div>
    <div class="contact">
      <p class="contact__name">Carl PENNER</p>
      <p class="contact__title">Managing Partner</p>
      <p class="contact__address">418 Harlow Ridge Rd 12 East<br>Milbrook ON, Canada, K0L 2H0</p>
      <ul class="contact__list">
        <li class="contact__item">
          <svg class="contact__icon contact__icon--solid" viewBox="0 0 12 12" aria-hidden="true"><path d="M2.5 0.8l2 2.2-1 1.3c.7 1.5 1.8 2.6 3.3 3.3l1.3-1 2.2 2-1.2 1.7C5 10 2 7 0.8 2z"/></svg>
          <span>555-271-4830 ext xxx</span>
        </li>
        <li class="contact__item">
          <svg class="contact__icon contact__icon--solid" viewBox="0 0 12 12" aria-hidden="true"><rect x="3" y="0.5" width="6" height="3"/><rect x="0.5" y="4" width="11" height="5" rx="1"/><rect x="3" y="8" width="6" height="3.5"/></svg>
          <span>555-271-4831</span>
        </li>
        <li class="contact__item">
          <svg class="contact__icon" viewBox="0 0 12 12" aria-hidden="true"><rect x="0.8" y="2.2" width="10.4" height="7.6"/><path d="M0.8 2.2l5.2 4.2 5.2-4.2"/></svg>
          <span>info@brixtelcore.com</span>
        </li>
        <li class="contact__item">
          <svg class="contact__icon" viewBox="0 0 12 12" aria-hidden="true"><circle cx="6" cy="6" r="5.2"/><ellipse cx="6" cy="6" rx="2.3" ry="5.2"/><path d="M0.8 6h10.4"/></svg>
          <span>www.brixtelcore.com</span>
        </li>
      </ul>
    </div>
  </section>
</main>
</body>
</html>
```